School Rules Posters

I would like a design for four different posters. Each one has a different purpose:

1: The Three Main rules

2: The Rewards

3: The Consequences

4: Consequences

At the moment they are very boring and dry and I would like an icon for each rule with the text underneath?

I'd like the logo on it.

It is for a middle school so it cannot be 'too young'.

I don't mind if the posters are Portrait or Landscape. The posters need to provide pupils with clarity and cannot be too busy. They'll be made into A1.
I have attached an example from another school which has logos - I don't want the same thing but give's you an idea of icons.

```html
<!DOCTYPE html>
<html lang="en">
<head>
<meta charset="utf-8">
<title>The Hartwell Way – Posters</title>
<link rel="stylesheet" href="https://fonts.googleapis.com/css2?family=Bebas+Neue&family=Source+Sans+3:wght@400;600;700;800&family=Dancing+Script:wght@700&display=swap">
<style>
:root{
  --bg:#d1d2d4;
  --paper:#ffffff;
  --plum:#962c7e;
  --plum-soft:#e9d6e3;
  --mauve:#876c89;
  --blue:#5f8fb6;
  --green:#7cab62;
  --gold:#dcb25c;
  --red:#c6505b;
  --amber:#f1b84a;
  --ink:#2b2230;
  --line:#ffffff;
}
*{box-sizing:border-box;margin:0;padding:0}
html,body{width:1200px;height:2239px;overflow:hidden;background:var(--bg)}
body{position:relative;font-family:"Source Sans 3",Arial,sans-serif;color:var(--ink)}
.poster{position:absolute;left:160px;width:842px;height:595px;background:var(--paper);box-shadow:6px 8px 8px rgba(0,0,0,.35)}
.poster--rules{top:163px}
.poster--rewards{top:829px}
.poster--consequences{top:1476px}

.title-band{position:absolute;left:20px;top:60px;width:800px;height:46px;background:var(--plum);border-radius:0 26px 26px 0}
.poster--consequences .title-band,.poster--rewards .title-band{width:802px}
.title{position:absolute;left:155px;top:60px;height:46px;line-height:48px;color:#fff;font-weight:800;font-size:35px;letter-spacing:-.3px;white-space:nowrap}
.tagline{position:absolute;left:152px;top:106px;font-family:"Dancing Script",cursive;font-size:23px;color:var(--ink)}
.brand{position:absolute;left:28px;top:26px;width:94px;height:116px;background:#fff;display:flex;flex-direction:column;align-items:center;justify-content:center;gap:8px}
.brand__mark{width:56px;height:56px;background:var(--plum)}
.brand__name{font-weight:700;font-size:10px;color:var(--plum);text-align:center;line-height:1.1;letter-spacing:.3px}

/* rules */
.rules-grid{position:absolute;left:20px;top:170px;width:802px;height:372px;display:grid;grid-template-columns:133px repeat(5,1fr);grid-template-rows:repeat(3,1fr);gap:0}
.rule-label{color:#fff;font-family:"Bebas Neue",sans-serif;font-size:36px;line-height:44px;padding:14px 0 0 15px;display:flex;align-items:center}
.rule-label--ready{background:linear-gradient(135deg,var(--plum) 55%,#b35a9c);border-radius:16px 0 0 0}
.rule-label--respect{background:linear-gradient(135deg,var(--blue) 55%,#86acc9)}
.rule-label--safe{background:linear-gradient(135deg,var(--green) 55%,#9cc385);border-radius:0 0 0 16px}
.rule{background:var(--plum-soft);border-left:1px solid var(--line);border-bottom:1px solid var(--line);display:flex;flex-direction:column;align-items:center;padding-top:16px;text-align:center;color:var(--plum)}
.rule--alt{background:var(--mauve);color:#fff}
.rule svg{width:52px;height:52px;fill:none;stroke:currentColor;stroke-width:2.2;stroke-linecap:round;stroke-linejoin:round}
.rule p{margin-top:14px;font-size:11.5px;line-height:14px;font-weight:600;color:var(--ink)}
.rule--alt p{color:#fff}

/* rewards */
.rewards{position:absolute;left:20px;top:176px;width:802px;height:376px;display:grid;grid-template-columns:repeat(4,1fr)}
.reward{position:relative;background:var(--plum-soft);border-left:1px solid var(--line)}
.reward:first-child{border-left:0}
.reward__head{height:123px;color:#fff;font-family:"Bebas Neue",sans-serif;font-weight:400;font-size:27px;line-height:30px;text-align:center;display:flex;align-items:flex-end;justify-content:center;padding-bottom:12px}
.reward--house .reward__head{background:linear-gradient(135deg,var(--plum) 60%,#b562a1);border-radius:16px 0 0 0;padding-bottom:14px}
.reward--council .reward__head{background:linear-gradient(135deg,var(--green) 60%,#a0c58b)}
.reward--subject .reward__head{background:linear-gradient(135deg,var(--gold) 60%,#e7c98b)}
.reward--year .reward__head{background:linear-gradient(135deg,var(--blue) 60%,#8db0cc);border-radius:0 16px 0 0}
.reward__badge{position:absolute;left:50%;top:-24px;width:76px;height:76px;margin-left:-38px;border-radius:50%;border:3px solid #fff;display:flex;align-items:center;justify-content:center}
.reward--house .reward__badge{background:var(--plum)}
.reward--council .reward__badge{background:var(--green)}
.reward--subject .reward__badge{background:var(--gold)}
.reward--year .reward__badge{background:var(--blue)}
.reward__badge svg{width:42px;height:42px;fill:none;stroke:#fff;stroke-width:2.2;stroke-linejoin:round;stroke-linecap:round}
.reward__body{padding:18px 18px 0 17px;font-size:12.4px;line-height:16px}
.reward__body p+p{margin-top:46px}

/* consequences */
.steps-side{position:absolute;left:20px;top:165px;width:42px;height:409px;background:var(--plum);border-radius:16px 0 0 16px}
.steps-side span{position:absolute;left:6px;width:30px;color:#fff;font-weight:700;font-size:10.5px;line-height:12px;writing-mode:vertical-rl;transform:rotate(180deg);text-align:center}
.steps-side .side-a{top:140px;height:130px}
.steps-side .side-b{top:275px;height:130px}
.steps-side hr{position:absolute;left:7px;top:273px;width:28px;border:0;border-top:1px solid #fff}
.steps{position:absolute;left:62px;top:165px;width:760px;height:409px;display:grid;grid-template-columns:repeat(6,1fr);grid-template-rows:30px 108px 137px 134px}
.step-head{color:#fff;font-weight:700;font-size:15px;text-align:center;line-height:30px;border-left:1px solid var(--line)}
.step-head--1{background:var(--mauve)}
.step-head--2{background:var(--blue)}
.step-head--3{background:var(--red)}
.step-head--4{background:var(--amber)}
.step-head--5{background:var(--green)}
.step-head--6{background:var(--plum)}
.step-cell{background:var(--plum-soft);border-left:1px solid var(--line);border-top:1px solid var(--line);font-size:9.3px;line-height:16px;padding:24px 10px 0 12px}
.step-icon{display:flex;flex-direction:column;align-items:center;justify-content:flex-start;padding:12px 6px 0;text-align:center;color:#7d7080}
.step-icon svg{width:36px;height:36px;fill:none;stroke:#7d7080;stroke-width:2;stroke-linecap:round;stroke-linejoin:round}
.step-icon p{font-size:9px;line-height:16px;font-weight:700;min-height:48px;display:flex;align-items:center;justify-content:center}
.step-cell--teacher{padding-top:58px}
</style>
</head>
<body>

<!-- RULES -->
<section class="poster poster--rules">
  <div class="title-band"></div>
  <div class="brand"><span class="brand__mark"></span><span class="brand__name">HARTWELL FENMOOR</span></div>
  <h1 class="title">THE HARTWELL WAY – RULES</h1>
  <p class="tagline">Helping us be the best we can be</p>

  <div class="rules-grid">
    <div class="rule-label rule-label--ready">BE READY</div>
    <div class="rule"><svg viewBox="0 0 52 52"><circle cx="28" cy="30" r="15"/><path d="M28 30V21M28 30l6 4M24 10h8M28 10v5M40 16l3-3"/><path d="M4 22h8M6 28h6M4 34h8"/></svg><p>Punctual to<br>meet and great</p></div>
    <div class="rule"><svg viewBox="0 0 52 52"><path d="M26 10a12 12 0 0 0-7 22v5h14v-5a12 12 0 0 0-7-22zM21 41h10M23 45h6M26 2v4M10 10l3 3M42 10l-3 3M4 24h5M43 24h5"/></svg><p>Ready to learn<br>new ideas</p></div>
    <div class="rule"><svg viewBox="0 0 52 52"><circle cx="26" cy="10" r="5"/><path d="M16 22h20l-3 8H19zM8 30h36M14 30l4 12h16l4-12M20 42v6M32 42v6"/></svg><p>Be Well-<br>Presented</p></div>
    <div class="rule"><svg viewBox="0 0 52 52"><circle cx="14" cy="12" r="7"/><circle cx="18" cy="34" r="6"/><circle cx="40" cy="28" r="4"/><path d="M20 16l16 10M24 33l12-4"/></svg><p>Have the right<br>equipment</p></div>
    <div class="rule"><svg viewBox="0 0 52 52"><rect x="16" y="4" width="22" height="14" rx="2"/><path d="M10 24h34M14 24v22M40 24v22M14 34h26M20 18v6M34 18v6"/></svg><p>Know your<br>seat</p></div>

    <div class="rule-label rule-label--respect">BE RESPE-<br>CTFUL</div>
    <div class="rule rule--alt"><svg viewBox="0 0 52 52"><path d="M16 30V12a3 3 0 0 1 6 0v12V8a3 3 0 0 1 6 0v16V10a3 3 0 0 1 6 0v16-8a3 3 0 0 1 6 0v14c0 10-6 16-14 16s-12-4-16-12l-4-8a3 3 0 0 1 5-3z"/></svg><p>Raise your<br>hand to talk</p></div>
    <div class="rule rule--alt"><svg viewBox="0 0 52 52"><path d="M2 20l10-6 8 4 8-4 10 2 12 6-4 8M6 24l4 10 10 8a3 3 0 0 0 4-3l2 2a3 3 0 0 0 4-3 3 3 0 0 0 4-3 3 3 0 0 0 4-4l-10-10-6 3"/></svg><p>Manners give<br>a great<br>impressions</p></div>
    <div class="rule rule--alt"><svg viewBox="0 0 52 52"><rect x="13" y="3" width="26" height="46"/><rect x="17" y="7" width="8" height="16"/><rect x="27" y="7" width="8" height="16"/><path d="M34 30v4"/></svg><p>Hold doors<br>open for<br>others</p></div>
    <div class="rule rule--alt"><svg viewBox="0 0 52 52"><circle cx="14" cy="12" r="6"/><circle cx="26" cy="10" r="5"/><circle cx="36" cy="32" r="10"/><path d="M36 26v6l4 3M8 30h14v16H8z"/></svg><p>Respect every<br>persons right<br>to learn and work</p></div>
    <div class="rule rule--alt"><svg viewBox="0 0 52 52"><circle cx="26" cy="14" r="8"/><path d="M10 44v-6a10 10 0 0 1 10-10h12a10 10 0 0 1 10 10v6zM22 36h8"/></svg><p>Show the best<br>version of you</p></div>

    <div class="rule-label rule-label--safe">BE SAFE</div>
    <div class="rule"><svg viewBox="0 0 52 52"><circle cx="26" cy="6" r="4"/><path d="M22 14h8l2 16h-3l-1 18h-4l-1-18h-3zM22 14l-4 12M30 14l4 12"/></svg><p>Walk quietly<br>around the school<br>building and grounds</p></div>
    <div class="rule"><svg viewBox="0 0 52 52"><circle cx="32" cy="6" r="4"/><path d="M28 14h8v18h-2v16h-6V28M28 18l-8 6M6 22h14l-2 24H8z"/></svg><p>Throw litter<br>in the bin</p></div>
    <div class="rule"><svg viewBox="0 0 52 52"><path d="M6 10h40v8H6zM6 14h40M12 28h28M14 28v16M38 28v16M8 30v14M44 30v14M22 32h8v8h-8z"/></svg><p>Eat and drink<br>in the designated<br>areas</p></div>
    <div class="rule"><svg viewBox="0 0 52 52"><rect x="16" y="4" width="20" height="12" rx="2"/><path d="M8 22h36l-4 8H12zM14 30v18M38 30v18M14 40h24"/></svg><p>Leave your<br>desk tidy for<br>the next class</p></div>
    <div class="rule"><svg viewBox="0 0 52 52"><path d="M4 48h44M6 20h40v28H6zM16 20l10-8 10 8M26 12V4h6v4h-6"/><rect x="10" y="25" width="6" height="5"/><rect x="20" y="25" width="6" height="5"/><rect x="30" y="25" width="6" height="5"/><rect x="40" y="25" width="3" height="5"/><rect x="10" y="35" width="6" height="5"/><rect x="30" y="35" width="6" height="5"/><rect x="22" y="38" width="8" height="10"/></svg><p>Look after our<br>building and<br>grounds</p></div>
  </div>
</section>

<!-- REWARDS -->
<section class="poster poster--rewards">
  <div class="title-band"></div>
  <div class="brand"><span class="brand__mark"></span><span class="brand__name">HARTWELL FENMOOR</span></div>
  <h1 class="title">THE HARTWELL WAY – REWARDS</h1>
  <p class="tagline">Celebrating when we are at our best</p>

  <div class="rewards">
    <article class="reward reward--house">
      <div class="reward__badge"><svg viewBox="0 0 42 42"><rect x="8" y="6" width="26" height="32" rx="2"/><path d="M16 3h10v6H16zM13 16l2 2 3-3M21 17h9M13 24l2 2 3-3M21 25h9M13 32l2 2 3-3M21 33h9"/></svg></div>
      <h2 class="reward__head">HOUSE POINTS</h2>
      <div class="reward__body"><p>Class Teachers can award house points for great learning, participating in clubs, acts of kindness, going above the expected standard</p><p>House Points can be spent in the school shop</p></div>
    </article>
    <article class="reward reward--council">
      <div class="reward__badge"><svg viewBox="0 0 42 42"><rect x="5" y="6" width="30" height="24"/><path d="M10 13h18M10 18h10"/><circle cx="28" cy="26" r="6"/><path d="M25 31l-2 8 5-3 5 3-2-8"/></svg></div>
      <h2 class="reward__head">SCHOOL COUNCILLOR<br>CERTIFICATE</h2>
      <div class="reward__body"><p>Anyone can recommend a certificate for their peer in recognition of a positive behaviour choice</p><p>A certificate is awarded in assembly and sent to your family</p></div>
    </article>
    <article class="reward reward--subject">
      <div class="reward__badge"><svg viewBox="0 0 42 42"><path d="M10 5h24v32H10zM16 5v14l4-3 4 3V5"/></svg></div>
      <h2 class="reward__head">SCHOOL COUNCILLOR<br>CERTIFICATE</h2>
      <div class="reward__body"><p>Subject Leaders can award certificates for great subject knowledge and learning</p><p>A certificate is awarded in assembly and sent to your family</p></div>
    </article>
    <article class="reward reward--year">
      <div class="reward__badge"><svg viewBox="0 0 42 42"><path d="M12 6h20v30H12zM8 10v28h20M16 12h12M16 17h12M16 22h12M16 27h8"/></svg></div>
      <h2 class="reward__head">HEAD OF YEAR<br>CERTIFICATES</h2>
      <div class="reward__body"><p>Heads of Year award certifi-cates for outstanding learners who have excelled in more than one area.</p><p>A certificate is awarded in assembly and sent to your family. You will have a hot chocolate with the head teacher</p></div>
    </article>
  </div>
</section>

<!-- CONSEQUENCES -->
<section class="poster poster--consequences">
  <div class="title-band"></div>
  <div class="brand"><span class="brand__mark"></span><span class="brand__name">HARTWELL FENMOOR</span></div>
  <h1 class="title">THE HARTWELL WAY – CONSEQUENCES</h1>
  <p class="tagline">Learning from our mistakes to be our best</p>

  <div class="steps-side">
    <span class="side-a" style="top:150px">HOW CAN I<br>HELP MYSELF</span>
    <hr>
    <span class="side-b">HOW CAN MY<br>TEACHER HELP ME</span>
  </div>

  <div class="steps">
    <div class="step-head step-head--1">STEP 1</div>
    <div class="step-head step-head--2">STEP 2</div>
    <div class="step-head step-head--3">STEP 3</div>
    <div class="step-head step-head--4">STEP 4</div>
    <div class="step-head step-head--5">STEP 5</div>
    <div class="step-head step-head--6">STEP 6</div>

    <div class="step-cell step-icon"><svg viewBox="0 0 36 36"><path d="M18 9a7 7 0 0 0-4 13v3h8v-3a7 7 0 0 0-4-13zM15 29h6M18 2v3M7 8l2 2M29 8l-2 2M3 16h3M30 16h3"/></svg><p>Recognising your<br>behaviour is stopping<br>you or others learn.</p></div>
    <div class="step-cell step-icon"><svg viewBox="0 0 36 36"><rect x="5" y="7" width="26" height="24" rx="2"/><path d="M5 13h26M11 4v5M25 4v5M10 18h4M16 18h4M22 18h4M10 24h4M16 24h4M22 24h4"/></svg><p>Reminder of<br>Expectations</p></div>
    <div class="step-cell step-icon"><svg viewBox="0 0 36 36"><path d="M18 4L33 31H3zM18 14v8M18 26v1"/></svg><p>Caution</p></div>
    <div class="step-cell step-icon"><svg viewBox="0 0 36 36"><circle cx="18" cy="19" r="12"/><path d="M18 12v7l5 3M8 5l-4 4M28 5l4 4M10 31l-3 3M26 31l3 3"/></svg><p>Last Chance</p></div>
    <div class="step-cell step-icon"><svg viewBox="0 0 36 36"><circle cx="18" cy="10" r="6"/><path d="M6 32v-5a8 8 0 0 1 8-8h8a8 8 0 0 1 8 8v5zM12 27h3M17 27h3M22 27h3"/></svg><p>Consequence</p></div>
    <div class="step-cell step-icon"><svg viewBox="0 0 36 36"><circle cx="11" cy="13" r="6"/><circle cx="25" cy="22" r="5"/><circle cx="30" cy="9" r="3"/><path d="M11 4v3M11 19v3M2 13h3M17 13h3"/></svg><p>Repair</p></div>

    <div class="step-cell">Refocus on my learning. Seek help if I don't understand the learning task and show me at my best.</div>
    <div class="step-cell">Listen to the reminder and refocus on my learning. Seek help if I don't understand the learning task and still show the best me.</div>
    <div class="step-cell">Listen to the choice and consequence and refocus on my learning and still show the best me.</div>
    <div class="step-cell">Listen to the choice and consequence and refocus on my learning – and still show the best me.</div>
    <div class="step-cell">Accept the consequence and still show the best me.</div>
    <div class="step-cell">Work with the teachers and peers to reflect on my choices and share what was happening for me.</div>

    <div class="step-cell step-cell--teacher">Help me understand the learning task and what is expected of me</div>
    <div class="step-cell step-cell--teacher">Remind me of the rules, delivered privately</div>
    <div class="step-cell step-cell--teacher">Remind me of the rules, delivered privately</div>
    <div class="step-cell step-cell--teacher">Give a 'choice &amp; conse-quence' and some take up time</div>
    <div class="step-cell step-cell--teacher">Give a consequence and an opportunity to repair</div>
    <div class="step-cell step-cell--teacher">Discuss how to help me make better choices next time.</div>
  </div>
</section>

</body>
</html>
```